Redesign B2B website

We are redesigning/ restructuring our current website. We provide company feedback surveys. We claim to be market leader in our country.
We like to be seen as a trustworthy, reliable and innovative partner to the top 1500 companies in the netherlands.
We want to be seen as a personal company.
Current website http://www.brunsvold.nl does not meet our standards mentioned above.
Updates
Added Homepage layout. Please check
Target Market(s)
Large businesses, HR, decisiontakers
Industry/Entity Type
It Company
Requirements
Must have
- -The website is intended to be responsive. please take that into account. (propose plonkav.es)
-The design should match our Style colors(will be provided)
- Wireframes are provided. Fonts used are Open Sans and Esteban,. Feel free to change things around.
Nice to have
- We like the design to be "flat", not much 3d effects, or icons.
Minimalist, Wordpress style or Metro style.

```html
<!DOCTYPE html>
<html lang="nl">
<head>
<meta charset="utf-8">
<title>Brunsvold – Medewerkers- en klantenonderzoek</title>
<link href="https://fonts.googleapis.com/css2?family=PT+Sans:ital,wght@0,400;0,700;1,400&display=swap" rel="stylesheet">
<style>
:root{
  --navy:#0b3a6e;
  --navy-deep:#0c2b5e;
  --teal:#0f8b8d;
  --teal-btn:#0e8a84;
  --page:#ececec;
  --text:#333;
  --muted:#8a8a8a;
  --foot:#3b3b3b;
  --foot-bottom:#2f2f2f;
  --gold:#e6b94c;
}
*{box-sizing:border-box;margin:0;padding:0}
html,body{width:986px;height:1200px;overflow:hidden}
body{font-family:"PT Sans",sans-serif;background:var(--page);color:var(--text);position:relative}
.abs{position:absolute}
ul{list-style:none}

.site-header{left:0;top:0;width:986px;height:75px;background:linear-gradient(100deg,var(--navy) 0%,#0d5c82 30%,#18a3a0 52%,#0f6f8d 70%,var(--navy) 85%)}
.brand{left:75px;top:22px;width:182px;height:33px;background:#fff;border:2px solid var(--navy);display:flex;align-items:center;justify-content:center;gap:8px;color:var(--navy);font-weight:700;font-size:20px;letter-spacing:1px}
.brand .dot{width:12px;height:12px;border-radius:50%;background:var(--navy)}
.social{display:flex;gap:7px}
.social span{width:24px;height:24px;border-radius:50%;background:#fff;display:block;border:3px solid #e8e8e8}
.social-top{left:766px;top:25px}

.main-nav{left:0;top:75px;width:986px;height:58px}
.main-nav .tab{left:73px;top:0;width:98px;height:58px;background:#f7f7f7}
.main-nav a{position:absolute;top:24px;font-size:12px;color:var(--teal);text-decoration:none}
.main-nav a.active{color:#222}
.search{left:764px;top:91px;width:148px;height:26px;background:#fff;border:1px solid #cfcfcf;font-size:10px;font-style:italic;color:#aaa;padding:6px 13px}
.search svg{position:absolute;right:8px;top:8px}

.sub-nav{left:73px;top:132px;width:840px;height:32px;background:#fff}
.sub-nav li{position:absolute;top:10px;font-size:11px;color:#333}
.sub-nav li::before{content:"";display:inline-block;width:4px;height:4px;border-radius:50%;background:currentColor;margin-right:9px;vertical-align:middle}
.sub-nav li.active{color:#1aa3a6}

.hero{left:73px;top:168px;width:840px;height:259px;background:#fff}
.hero h1{left:24px;top:26px;width:420px;font-size:20px;font-weight:400;line-height:29px;color:var(--teal)}
.hero p{left:24px;top:97px;width:400px;font-size:10.5px;line-height:19px;color:#333;text-align:justify}
.btn{left:25px;top:190px;width:126px;height:35px;background:var(--teal-btn);border-radius:2px;color:#fff;font-size:13px;padding:9px 0 0 12px}
.btn i{position:absolute;right:15px;top:10px;width:15px;height:15px;border-radius:50%;background:#e8e8e8}
.btn i::after{content:"";position:absolute;left:6px;top:4px;border-left:5px solid #444;border-top:3.5px solid transparent;border-bottom:3.5px solid transparent}
.hero-photo{left:461px;top:12px;width:361px;height:234px;border:6px solid #e2e2e2;background:linear-gradient(135deg,#e9eef2,#c7d3dc 45%,#9eb1c4 70%,#dfe6ec)}

.contact-tab{left:941px;top:310px;width:45px;height:120px;background:#333;border-radius:4px 0 0 4px;color:#fff}
.contact-tab span{position:absolute;left:8px;top:72px;transform:rotate(-90deg);transform-origin:left top;font-size:19px;top:78px;left:12px}

.feature{left:81px;width:440px;height:90px}
.feature .thumb{left:0;top:0;width:82px;height:76px;border:1px solid #d0d0d0;background:linear-gradient(160deg,#dfe5ea,#8ea2b6)}
.feature h2{left:100px;top:0;font-size:19px;font-weight:400;color:var(--teal)}
.feature p{left:100px;top:28px;width:334px;font-size:10.5px;line-height:17px;text-align:justify}

.quote{left:566px;top:466px;width:322px;font-size:18px;font-style:italic;line-height:29px;color:#8a8a8a;text-align:justify}
.quote b{font-weight:700;color:#c8c8c8;font-size:24px;font-style:normal}
.author{left:700px;top:620px;width:187px;text-align:right;font-size:11.5px;color:var(--teal)}
.partner{background:#b8b8b8}

.news-band{left:0;top:818px;width:986px;height:71px;background:var(--navy-deep)}
.social-foot{left:76px;top:843px}
.news-label{left:548px;top:846px;font-size:12px;font-style:italic;color:#e6eef8}
.news-form{left:712px;top:839px;width:200px;height:27px;background:#fff;border-radius:2px;font-size:10px;font-style:italic;color:#999;padding:7px 12px}
.news-form span{position:absolute;right:4px;top:4px;width:56px;height:19px;background:#333;border-radius:10px;color:#fff;font-size:10px;text-align:center;line-height:19px}

.site-footer{left:0;top:889px;width:986px;height:251px;background:var(--foot)}
.col{top:30px}
.col h3{font-size:11.5px;font-weight:400;color:var(--gold);margin-bottom:12px}
.col li{font-size:10.5px;color:#e8e8e8;line-height:20.6px;padding-left:14px;position:relative}
.col li::before{content:"";position:absolute;left:2px;top:9px;width:3px;height:3px;border-radius:50%;background:#ddd}

.legal{left:0;top:1140px;width:986px;height:60px;background:var(--foot-bottom);color:#9a9a9a;font-size:10.5px;text-align:center;padding-top:23px;word-spacing:1px}
.legal em{font-style:normal;margin:0 16px}
</style>
</head>
<body>

<header class="site-header abs">
  <div class="brand abs">BRUNSVOLD <span class="dot"></span></div>
  <div class="social social-top abs" aria-label="Sociale media"><span></span><span></span><span></span><span></span><span></span></div>
</header>

<nav class="main-nav abs">
  <div class="tab abs"></div>
  <a class="active" style="left:90px">PRODUCTEN</a>
  <a style="left:194px">OPLOSSINGEN</a>
  <a style="left:308px">BRANCHES</a>
  <a style="left:403px">KENNIS</a>
  <a style="left:481px">KLANTEN</a>
  <a style="left:569px">OVER BRUNSVOLD</a>
</nav>
<div class="search abs">Zoeken
  <svg width="10" height="10" viewBox="0 0 10 10"><circle cx="4" cy="4" r="3" fill="none" stroke="#bbb" stroke-width="1.3"/><line x1="6.2" y1="6.2" x2="9" y2="9" stroke="#bbb" stroke-width="1.5"/></svg>
</div>

<ul class="sub-nav abs">
  <li class="active" style="left:18px">Drop Link1</li>
  <li style="left:122px">Drop Link1</li>
  <li style="left:234px">Drop Link1</li>
  <li style="left:338px">Drop Link1</li>
  <li style="left:441px">Drop Link1</li>
</ul>

<section class="hero abs">
  <h1 class="abs">Bevlogenheid en betrokkenheid stimuleren binnen uw organisatie?</h1>
  <p class="abs">Sed ut perspiciatis unde omnis iste natus error sit voluptatem accusantium doloremque laudantium, totam rem aperiam, eaque ipsa quae ab illo inventore veritatis et quasi architecto beatae vitae dicta sunt explicabo. Nemo enim ipsam voluptatem quia voluptas sit aspernatur aut odit aut fugit, sed quia consequuntur.</p>
  <div class="btn abs">Gratis eBook <i></i></div>
  <div class="hero-photo abs" role="img" aria-label="Foto: collega's in een vergadering die lachend applaudisseren"></div>
</section>

<div class="contact-tab abs"><span>Contact</span></div>

<article class="feature abs" style="top:472px">
  <div class="thumb abs" role="img" aria-label="Foto: zakenvrouw aan de telefoon"></div>
  <h2 class="abs">Een onderzoek dat bij u past</h2>
  <p class="abs">Eaque ipsa quae ab illo inventore veritatis et quasi architecto beatae vitae dicta sunt explicabo. Nemo enim ipsam voluptatem quia voluptas sit aspernatur aut odit aut fugit, sed quia consequuntur.</p>
</article>
<article class="feature abs" style="top:584px">
  <div class="thumb abs" role="img" aria-label="Foto: medewerkers aan het werk in een kantoor"></div>
  <h2 class="abs">Uw scores in perspectief met uw branche</h2>
  <p class="abs">Eaque ipsa quae ab illo inventore veritatis et quasi architecto beatae vitae dicta sunt explicabo. Nemo enim ipsam voluptatem quia voluptas sit aspernatur aut odit aut fugit, sed quia consequuntur.</p>
</article>
<article class="feature abs" style="top:696px">
  <div class="thumb abs" role="img" aria-label="Foto: lachende zakenman met collega op de achtergrond"></div>
  <h2 class="abs">Aan de slag met de resultaten</h2>
  <p class="abs">Eaque ipsa quae ab illo inventore veritatis et quasi architecto beatae vitae dicta sunt explicabo. Nemo enim ipsam voluptatem quia voluptas sit aspernatur aut odit aut fugit, sed quia consequuntur.</p>
</article>

<blockquote class="quote abs"><b>“</b> Medewerkers kunnen zich pas echt thuds voelen ale ze weten waar de organisatie voor stoat. En dat is be¬langrijk want betrokken medewerk¬ers zijn productief en blijven langer bij de organisatie. <b>”</b></blockquote>
<div class="author abs">Daan Verhoef, CEO Noordlicht</div>

<div aria-label="Klanten">
  <div class="partner abs" style="left:574px;top:662px;width:48px;height:40px"></div>
  <div class="partner abs" style="left:628px;top:660px;width:28px;height:42px;border-radius:4px 4px 14px 14px"></div>
  <div class="partner abs" style="left:667px;top:670px;width:78px;height:22px;border-radius:4px"></div>
  <div class="partner abs" style="left:754px;top:662px;width:28px;height:38px;border-radius:50%"></div>
  <div class="partner abs" style="left:790px;top:670px;width:88px;height:24px;border-radius:12px"></div>
  <div class="partner abs" style="left:566px;top:738px;width:88px;height:20px;border-radius:3px"></div>
  <div class="partner abs" style="left:662px;top:730px;width:36px;height:36px;border-radius:3px"></div>
  <div class="partner abs" style="left:712px;top:734px;width:52px;height:32px"></div>
  <div class="partner abs" style="left:776px;top:733px;width:58px;height:34px;border-radius:50%"></div>
  <div class="partner abs" style="left:842px;top:734px;width:44px;height:32px;border-radius:3px"></div>
</div>

<section class="news-band abs">
  <div class="social social-foot abs" aria-label="Sociale media"><span></span><span></span><span></span><span></span><span></span></div>
  <div class="news-label abs" style="top:28px">Schrijfje error cote niewsbrief</div>
  <div class="news-form abs" style="top:21px">Enter your mail ID <span>SUBMIT</span></div>
</section>

<footer class="site-footer abs">
  <div class="col abs" style="left:77px"><h3>Wat doen wij</h3><ul>
    <li>Totaalpallet Feedback</li><li>Medewekersonderzoek</li><li>Klantenderzoek</li><li>Intem Klantenonderzoek</li></ul></div>
  <div class="col abs" style="left:296px"><h3>Waar Kunnen we mee helpen</h3><ul>
    <li>Totaalpallet Feedback</li><li>Medewekersonderzoek</li><li>Klantenderzoek</li><li>Intem Klantenonderzoek</li><li>Totaalpallet Feedback</li><li>Medewekersonderzoek</li><li>Klantenderzoek</li><li>Intem Klantenonderzoek</li><li>Bevlogen en betrokken medewerkers</li></ul></div>
  <div class="col abs" style="left:571px"><h3>Ruime ervaring in</h3><ul>
    <li>Financiele dienstverlenming</li><li>Klantenderzoek</li><li>Intem Klantenonderzoek</li><li>Totaalpallet Feedback</li><li>Retail</li><li>Klantenderzoek</li><li>Intem Klantenonderzoek</li><li>Totaalpallet Feedback</li><li>Zorg en welzijn</li></ul></div>
  <div class="col abs" style="left:803px"><h3>Meer over ons</h3><ul>
    <li>Onze Klanten</li><li>Over Brunsvold</li><li>Kennisbank</li><li>Blog</li><li>Werken bij Brunsvold</li></ul></div>
</footer>

<div class="legal abs">Copyright © 2012 www.brunsvold.nl. Medewerkers - en klantenonderzoek <em>|</em> Privacy-en Cookiebeleid <em>|</em> Algemene Voorwaarden</div>

</body>
</html>
```